Wine Label Design

We need a wine label design with the following characteristics:
- Round
- I've attached a photo of a rough design
- The writing:
--- Twin Ks
---Crafted by Lu Venkova
-----Pinwheel Chardonnay
------Dundee Hills
-----2021
- We'd like a couple of options on the background color:
- Pale mint green
- Cream
- Lettering a dark gray
- The three cursive Ms should kinda look like mountains
- Size: 3"x3"

```html
<!DOCTYPE html>
<html lang="en">
<head>
<meta charset="utf-8">
<title>Twin Ks – Pinwheel Chardonnay Label Options</title>
<link rel="stylesheet" href="https://fonts.googleapis.com/css2?family=Josefin+Sans:wght@400;600&family=Tenor+Sans&display=swap">
<style>
  :root {
    --ink: #58595b;
    --page: #ffffff;
    --ring: #f1f8f3;
    --mint-band: #b9f2d6;
    --mint-field: #cff6df;
    --cream-band: #efe6bd;
    --cream-field: #f6efd3;
    --flourish: rgba(255, 255, 255, 0.45);
  }
  html, body {
    margin: 0;
    padding: 0;
    width: 1200px;
    height: 800px;
    overflow: hidden;
    background: var(--page);
  }
  .label-sheet {
    display: block;
    width: 1200px;
    height: 800px;
  }
  .label--mint { --band: var(--mint-band); --field: var(--mint-field); }
  .label--cream { --band: var(--cream-band); --field: var(--cream-field); }
  .label-band { fill: var(--band); }
  .label-field { fill: var(--field); stroke: var(--ring); stroke-width: 4; }
  .label-flourish { fill: var(--flourish); }
  .winery-name {
    font-family: "Josefin Sans", sans-serif;
    font-weight: 400;
    font-size: 42px;
    letter-spacing: 8px;
    fill: var(--ink);
  }
  .winery-centre {
    font-family: "Josefin Sans", sans-serif;
    font-weight: 400;
    font-size: 58px;
    letter-spacing: 6px;
    fill: var(--ink);
  }
  .side-line {
    font-family: "Tenor Sans", sans-serif;
    font-size: 19px;
    letter-spacing: 0.5px;
    fill: var(--ink);
  }
  .region {
    font-family: "Josefin Sans", sans-serif;
    font-weight: 400;
    font-size: 28px;
    letter-spacing: 5px;
    fill: var(--ink);
  }
  .vintage {
    font-family: "Josefin Sans", sans-serif;
    font-weight: 600;
    font-size: 36px;
    letter-spacing: 7px;
    fill: var(--ink);
  }
</style>
</head>
<body>
<svg class="label-sheet" viewBox="0 0 1200 800" xmlns="http://www.w3.org/2000/svg" xmlns:xlink="http://www.w3.org/1999/xlink">
  <defs>
    <path id="arc-top" d="M -186 0 A 186 186 0 0 1 186 0"/>
    <path id="arc-bottom" d="M -186 0 A 186 186 0 0 0 186 0"/>
    <path id="arc-left" d="M -132.9 132.9 A 188 188 0 0 1 -132.9 -132.9"/>
    <path id="arc-right" d="M 132.9 -132.9 A 188 188 0 0 1 132.9 132.9"/>

    <g id="round-label">
      <circle class="label-band" r="238"/>
      <circle class="label-field" r="174"/>

      <g class="label-flourishes" role="img" aria-label="Decorative scroll flourishes at the four corners of the inner ring">
        <ellipse class="label-flourish" cx="-123" cy="-123" rx="26" ry="12" transform="rotate(-45 -123 -123)"/>
        <ellipse class="label-flourish" cx="123" cy="-123" rx="26" ry="12" transform="rotate(45 123 -123)"/>
        <ellipse class="label-flourish" cx="-123" cy="123" rx="26" ry="12" transform="rotate(45 -123 123)"/>
        <ellipse class="label-flourish" cx="123" cy="123" rx="26" ry="12" transform="rotate(-45 123 123)"/>
      </g>

      <text class="winery-name"><textPath xlink:href="#arc-top" href="#arc-top" startOffset="50%" text-anchor="middle">TWIN KS</textPath></text>
      <text class="side-line"><textPath xlink:href="#arc-left" href="#arc-left" startOffset="50%" text-anchor="middle">Pinwheel Chardonnay</textPath></text>
      <text class="side-line"><textPath xlink:href="#arc-right" href="#arc-right" startOffset="50%" text-anchor="middle">Crafted by Lu Venkova</textPath></text>
      <text class="region"><textPath xlink:href="#arc-bottom" href="#arc-bottom" startOffset="50%" text-anchor="middle" dominant-baseline="hanging">DUNDEE HILLS</textPath></text>

      <text class="winery-centre" x="0" y="0" text-anchor="middle">TWIN KS</text>
      <text class="vintage" x="4" y="118" text-anchor="middle">2021</text>
    </g>
  </defs>

  <use class="label label--mint" href="#round-label" xlink:href="#round-label" x="330" y="394"/>
  <use class="label label--cream" href="#round-label" xlink:href="#round-label" x="870" y="404"/>
</svg>
</body>
</html>
```